Wizards Among Humbug Trades*

I am looking for a book cover which will really pop. Working title: Wizards Among Humbug Trades (or W.A.H.T. for short) The concept behind the book is: education is too expensive, screwed up, and basically failing us, and even an MBA is not worth it's name anymore! How a BS is Brilliantly Stupid, a BA is great to be a Broke Artist, an MA is Mostly Antiquated and a MS Mastered Something? ...you get the point, basically I'll be ripping into a whole bunch of degree types, then walking you through what you should actually learn from an MBA. It is going to be written with a fair bit of humor, while still being fact driven. Target audience is working professionals who are considering an MBA, or have one and want a $15 refresher of all they spent $90k+ on. No color scheme is requested, Since i do like to allow creativity to flow!

Book size 5" by 8" and ebook. Author is: L.K. Brannigan size format attached.

Went on vacation/holiday

Colors

Requirements
Must have
• W.A.H.T. (but can be an emphasises in the Wizards Among Humbug Trades title.
Nice to have
• If you look at "A quiet orchard year: notes on tending pears while raising twin goats" on quorvel, you can see a blue/silver/white color scheme I liked in the past - but dont take that as a must by any means, the second choice was a completely different (red and white) scheme

```html
<!DOCTYPE html>
<html lang="en">
<head>
<meta charset="utf-8">
<title>Wizards Among Humbug Trades — Cover Wrap</title>
<link rel="stylesheet" href="https://fonts.googleapis.com/css2?family=Barlow+Condensed:wght@500;600;700&family=Barlow+Semi+Condensed:wght@600;700&family=Dosis:wght@300;400&display=swap">
<style>
  :root {
    --page: #ffffff;
    --blue-top: #0a8ad8;
    --blue-mid: #0670c4;
    --blue-deep: #073d86;
    --panel: #063a7e;
    --ink-light: #1f8fe0;
    --spine-title: #0b57a8;
    --spine-author: #1a7fd0;
    --cap-a: #5fe3c8;
    --cap-b: #e4f6fb;
    --white: #ffffff;
  }
  * { box-sizing: border-box; margin: 0; padding: 0; }
  html, body { width: 1200px; height: 1200px; overflow: hidden; background: var(--page); }
  .canvas { position: relative; width: 1200px; height: 1200px; background: var(--page); }

  .back-cover {
    position: absolute; left: 0; top: 160px; width: 572px; height: 874px;
    background: linear-gradient(180deg, var(--blue-top) 0%, var(--blue-mid) 55%, #0b62b8 100%);
  }
  .back-panel {
    position: absolute; left: 66px; top: 242px; width: 443px; height: 680px;
    background: var(--panel);
  }
  .blurb {
    position: absolute; left: 98px; width: 379px;
    font-family: "Dosis", sans-serif; font-weight: 300; font-size: 16px; line-height: 21.6px;
    color: var(--ink-light); text-align: justify; hyphens: auto;
  }
  .blurb--first { top: 275px; }
  .blurb--second { top: 492px; }
  .author-box {
    position: absolute; left: 98px; top: 640px; width: 382px; height: 178px;
    border: 1.5px solid var(--white); padding: 14px 12px 0 12px;
    color: var(--white); font-family: "Dosis", sans-serif;
  }
  .author-box__heading {
    text-align: center; font-weight: 400; font-size: 16px; letter-spacing: 2px; margin-bottom: 14px;
  }
  .author-box__text { font-weight: 400; font-size: 16.5px; line-height: 21.6px; text-align: justify; }
  .barcode-space { position: absolute; left: 342px; top: 874px; width: 205px; height: 122px; background: var(--white); }

  .spine { position: absolute; left: 572px; top: 160px; width: 56px; height: 874px; background: var(--white); }
  .spine__title, .spine__author {
    position: absolute; left: 50%; writing-mode: vertical-rl; transform: translateX(-50%);
    white-space: nowrap;
  }
  .spine__title {
    top: 28px; font-family: "Barlow Condensed", sans-serif; font-weight: 700; font-size: 29px;
    color: var(--spine-title); letter-spacing: -0.2px;
  }
  .spine__author {
    top: 612px; font-family: "Barlow Semi Condensed", sans-serif; font-weight: 700; font-size: 20px;
    color: var(--spine-author); letter-spacing: 6px;
  }

  .front-cover {
    position: absolute; left: 628px; top: 160px; width: 572px; height: 778px;
    background: linear-gradient(180deg, var(--blue-top) 0%, var(--blue-mid) 45%, var(--blue-deep) 100%);
  }
  .title-frame { position: absolute; left: 660px; top: 188px; width: 513px; height: 328px; border: 2px solid var(--white); }
  .title-acronym { position: absolute; left: 686px; top: 206px; width: 474px; height: 160px; }
  .title-acronym text {
    font-family: "Barlow Condensed", sans-serif; font-weight: 500; font-size: 200px;
    fill: none; stroke: var(--white); stroke-width: 2.5;
  }
  .title-words {
    position: absolute; left: 660px; top: 380px; width: 513px; text-align: center;
    font-family: "Barlow Condensed", sans-serif; font-weight: 700; font-size: 68px; line-height: 56px;
    color: var(--white); text-transform: uppercase;
  }
  .cap-art {
    position: absolute; left: 636px; top: 568px; width: 524px; height: 332px;
    background: linear-gradient(90deg, rgba(95,227,200,0.15) 0%, rgba(95,227,200,0.7) 30%, rgba(228,246,251,0.8) 75%, rgba(228,246,251,0.3) 100%);
    border-radius: 50% 40% 30% 40% / 40% 40% 60% 60%;
  }
  .author-band {
    position: absolute; left: 628px; top: 938px; width: 572px; height: 66px; background: var(--white);
    display: flex; align-items: center; justify-content: center;
    font-family: "Barlow Semi Condensed", sans-serif; font-weight: 700; font-size: 46px;
    letter-spacing: 0.33em; color: var(--panel); padding-left: 0.33em;
  }
  .base-band { position: absolute; left: 628px; top: 1004px; width: 572px; height: 30px; background: var(--panel); }
</style>
</head>
<body>
<main class="canvas">
  <section class="back-cover" role="img" aria-label="Blue background with faint hand-drawn business doodles: charts, clocks, gears and arrows"></section>
  <div class="back-panel"></div>
  <p class="blurb blurb--first">Lorem ipsum dolor sit amet, consectetur adipiscing elit, sed do eiusmod tempor incididunt ut labore et dolore magna aliqua. Ut enim ad minim veniam, quis nostrud exercitation ullamco laboris nisi ut aliquip ex ea commodo consequat. Duis aute irure dolor in reprehenderit in voluptate velit esse cillum dolore eu fugiat nulla pariatur. Excepteur sint occaecat cupidatat non proident, sunt in culpa qui officia deserunt mollit anim id est laborum.</p>
  <p class="blurb blurb--second">Lorem ipsum dolor sit amet, consectetur adipiscing elit, sed do eiusmod tempor incididunt ut labore et dolore magna aliqua. Ut enim ad minim veniam, quis nostrud exercitation ullamco laboris nisi ut aliquip ex ea commodo consequat.</p>
  <div class="author-box">
    <h2 class="author-box__heading">ABOUT THE AUTHOR</h2>
    <p class="author-box__text">Duis aute irure dolor in reprehenderit in voluptate velit esse cillum dolore eu fugiat nulla pariatur. Excepteur sint occaecat cupidatat non proident, sunt in culpa qui officia deserunt mollit anim id est laborum.</p>
  </div>
  <div class="barcode-space"></div>

  <aside class="spine">
    <span class="spine__title">WIZARDS AMONG HUMBUG TRADES</span>
    <span class="spine__author">L.K. BRANNIGAN</span>
  </aside>

  <section class="front-cover"></section>
  <div class="title-frame"></div>
  <svg class="title-acronym" viewBox="0 0 474 160" aria-label="W.A.H.T.">
    <text x="0" y="155" textLength="474" lengthAdjust="spacingAndGlyphs">W.A.H.T.</text>
  </svg>
  <h1 class="title-words">Wizards Among<br>Humbug Trades</h1>
  <div class="cap-art" role="img" aria-label="Pixelated graduation cap dissolving into teal squares on the left"></div>
  <div class="author-band">L.K. BRANNIGAN</div>
  <div class="base-band"></div>
</main>
</body>
</html>
```